The Pebble Lantern Business Card

I need a business card designed for The Pebble Lantern. The company provides on site support and education to end consumers in the ins and outs of all our digital devices. We advise on product purchase, installation, maintenance and troubleshooting. Anything from cordless phones to home networks.
My initial concept is double sided with the white logo on green on one side and contact details and a small logo on the flip side (logo package attached)
Contact Details:
Marty Fenwick
Managing Director
PO Box 3
Brindlewood, QLD 4209
Phone: 0438 605 193
email: marty@pebblelantern.com.au
web: www.pebblelantern.com.au
Target Market(s)
Busy professionals and retired folks.
Industry/Entity Type
Education
Look and feel

```html
<!DOCTYPE html>
<html lang="en">
<head>
<meta charset="utf-8">
<title>The Pebble Lantern – Business Card</title>
<link href="https://fonts.googleapis.com/css2?family=Fira+Sans:ital,wght@0,300;0,400;0,500;1,600&display=swap" rel="stylesheet">
<style>
  :root {
    --leaf-green: #79b536;
    --navy: #1e2b47;
    --card-white: #ffffff;
    --stage: #e9ece4;
    --soft-white: #f3f8ec;
  }
  * { box-sizing: border-box; margin: 0; padding: 0; }
  html, body {
    width: 1200px; height: 803px; overflow: hidden;
    background: var(--stage);
    font-family: "Fira Sans", sans-serif;
  }
  .canvas {
    position: relative; width: 1200px; height: 803px;
  }
  .card {
    position: absolute; top: 242px;
    width: 520px; height: 318px;
    border-radius: 6px; overflow: hidden;
    box-shadow: 0 6px 22px rgba(30, 43, 71, 0.18);
  }
  /* contact side */
  .card--contact { left: 60px; background: var(--card-white); }
  .card--contact .green-panel {
    position: absolute; inset: 0; width: 520px; height: 318px;
  }
  .brand-small {
    position: absolute; left: 34px; top: 128px; width: 170px;
    color: var(--navy); font-weight: 400; font-size: 25px; line-height: 1.1;
    text-transform: uppercase; letter-spacing: 1px;
  }
  .person {
    position: absolute; right: 40px; top: 26px; text-align: right;
  }
  .person__name {
    color: var(--card-white); font-weight: 400; font-size: 21px;
  }
  .person__role {
    color: var(--navy); font-style: italic; font-weight: 600; font-size: 14px; margin-top: 2px;
  }
  .contact-list {
    position: absolute; right: 20px; top: 142px; list-style: none;
  }
  .contact-list li {
    display: flex; align-items: center; justify-content: flex-end; gap: 10px;
    color: var(--soft-white); font-size: 13px; font-weight: 400; height: 24px;
  }
  .contact-list li.address { margin-top: 30px; font-size: 12px; }
  .contact-list svg { width: 18px; height: 18px; flex: none; }
  /* logo side */
  .card--logo { left: 620px; background: var(--leaf-green); }
  .brand-large {
    position: absolute; left: 0; right: 0; top: 50%; transform: translateY(-50%);
    text-align: center; color: var(--card-white);
    font-weight: 300; font-size: 44px; letter-spacing: 1px;
  }
</style>
</head>
<body>
<main class="canvas">

  <section class="card card--contact" aria-label="Business card, contact side">
    <svg class="green-panel" viewBox="0 0 520 318" aria-hidden="true">
      <path d="M238 0 H520 V318 H205 C160 272 168 196 222 140 C262 98 262 46 238 0 Z" fill="var(--leaf-green)"/>
    </svg>
    <div class="brand-small">The Pebble Lantern</div>
    <div class="person">
      <div class="person__name">Marty Fenwick</div>
      <div class="person__role">Managing Director</div>
    </div>
    <ul class="contact-list">
      <li>0438 605 193
        <svg viewBox="0 0 20 20" aria-hidden="true"><path d="M3 7 C3 4 17 4 17 7 V9 H13 V7 H7 V9 H3 Z M5 10 H15 L16 16 H4 Z" fill="var(--navy)"/><circle cx="10" cy="13" r="1.6" fill="var(--leaf-green)"/></svg>
      </li>
      <li>marty@pebblelantern.com.au
        <svg viewBox="0 0 20 20" aria-hidden="true"><rect x="2" y="4" width="16" height="12" fill="var(--navy)"/><path d="M2.5 4.5 L10 11 L17.5 4.5" stroke="var(--leaf-green)" stroke-width="1.4" fill="none"/></svg>
      </li>
      <li>www.pebblelantern.com.au
        <svg viewBox="0 0 20 20" aria-hidden="true"><circle cx="10" cy="10" r="8" fill="var(--navy)"/><ellipse cx="10" cy="10" rx="3.5" ry="8" stroke="var(--leaf-green)" stroke-width="1.2" fill="none"/><path d="M2 10 H18" stroke="var(--leaf-green)" stroke-width="1.2"/></svg>
      </li>
      <li class="address">PO Box 3, Brindlewood, QLD 4209
        <svg viewBox="0 0 20 20" aria-hidden="true"><path d="M10 1 C5.5 1 3 4.3 3 7.8 C3 12.5 10 19 10 19 C10 19 17 12.5 17 7.8 C17 4.3 14.5 1 10 1 Z" fill="var(--navy)"/><circle cx="10" cy="7.8" r="2.6" fill="var(--leaf-green)"/></svg>
      </li>
    </ul>
  </section>

  <section class="card card--logo" aria-label="Business card, logo side">
    <div class="brand-large">The Pebble Lantern</div>
  </section>

</main>
</body>
</html>
```